Zielgruppe
Ich habe derzeit 3 Geschäftsfelder:
-> HR Business Partner
-> Mediation
-> Coaching
Ich arbeite zum Einen prozesshaft und klar strukturiert, zum Anderen mit Kreativität und Empathie
Ich möchte Unternehmen bei diversen HR Aufgaben unterstützen wie z.B. Mitarbeitergespräche, Konfliktgespräche, Recruiting, Teambuilding, Prozessbegleitung und Workshops,...
als auch Unternehmen und Privatpersonen in Konfliktsituationen durch Mediationsprozesse führen (von Lehrlingsmediationen über Unternehmensübergaben und Wirtschaftsmediationen bis Paarmediationen, Nachbarschaftsmediationen, Familienmediationen,...)
Beim Coaching geht es um Karriere- und Bewerbungscoaching und auch Krisen- oder Beziehungscoaching (für Paare/ Familien)
In Zukunft möchte ich noch eine Ausbildung zur Outdoortrainerin machen um Teambuilding in der Natur anbieten zu können.
Aufgabenstellung
schlicht, unkompliziert, klare Struktur
nicht zu schnörkelig, verspielt
Naturbezug? ... eventuell als Schriftfarbe Rasen oder etwas in der Art als eyecatcher?
gut vorstellbar wären Farben in Kombination blau oder blaugrau mit grün?

```html
<!DOCTYPE html>
<html lang="de">
<head>
<meta charset="utf-8">
<title>Klarweg – Visitenkarte</title>
<link href="https://fonts.googleapis.com/css2?family=Montserrat:wght@300;400;500&display=swap" rel="stylesheet">
<style>
  :root{
    --backdrop:#c0bfbd;
    --navy:#0e4a72;
    --green:#8cc63f;
    --grey:#555;
    --white:#fff;
    --shadow:rgba(40,40,40,.75);
  }
  *{margin:0;padding:0;box-sizing:border-box}
  html,body{width:1200px;height:1176px;overflow:hidden}
  body{background:var(--backdrop);font-family:"Montserrat",sans-serif;position:relative}
  .card{position:absolute;box-shadow:14px 12px 10px var(--shadow)}
  .card--front{left:210px;top:63px;width:769px;height:488px;background:var(--white)}
  .card--back{left:221px;top:641px;width:774px;height:490px;background:var(--green)}

  .brand{position:absolute;display:flex;align-items:center}
  .brand__dot{border-radius:50%;background:var(--navy);flex:none}
  .brand__name{font-weight:500;color:var(--navy);letter-spacing:1px;line-height:1}
  .owner{position:absolute;display:flex;align-items:center;gap:16px;font-weight:300;color:var(--green)}
  .owner__rule{height:1px;background:currentColor;flex:1}

  .card--front .brand{left:120px;top:62px;gap:22px}
  .card--front .brand__dot{width:60px;height:60px}
  .card--front .brand__name{font-size:40px}
  .card--front .owner{left:247px;top:136px;width:426px;font-size:24px}

  .person{position:absolute;left:376px;top:210px}
  .person__name{font-size:36px;font-weight:400;color:var(--green);letter-spacing:1px;line-height:1}
  .person__role{margin-top:18px;margin-left:34px;font-size:15px;color:var(--grey);letter-spacing:4px}

  .address{position:absolute;left:20px;top:326px;display:flex;gap:12px;color:var(--navy);font-size:20px;line-height:26px}
  .contacts{position:absolute;left:376px;top:332px;list-style:none;color:var(--navy);font-size:20px}
  .contacts li{display:flex;align-items:center;gap:12px;height:26px;margin-bottom:16px}
  .accent-bar{position:absolute;left:376px;right:0;bottom:0;height:12px;background:var(--green)}

  .card--back .brand{left:40px;top:156px;gap:30px}
  .card--back .brand__dot{width:80px;height:80px;background:var(--navy)}
  .card--back .brand__name{font-size:54px}
  .card--back .owner{left:210px;top:260px;width:545px;font-size:32px;color:var(--white)}
</style>
</head>
<body>
  <section class="card card--front">
    <div class="brand">
      <span class="brand__dot"></span>
      <span class="brand__name">KLARWEG</span>
    </div>
    <div class="owner"><span class="owner__rule"></span><span>Mara Lindholm</span><span class="owner__rule"></span></div>

    <div class="person">
      <h1 class="person__name">YOUR NAME</h1>
      <p class="person__role">JOB POSITION</p>
    </div>

    <div class="address">
      <svg width="22" height="32" viewBox="0 0 22 32" aria-hidden="true"><path d="M11 1C5.5 1 1.5 5 1.5 10.5 1.5 17 11 31 11 31s9.5-14 9.5-20.5C20.5 5 16.5 1 11 1z" fill="var(--green)"/><circle cx="11" cy="10.5" r="4" fill="var(--white)"/></svg>
      <p>Your City Adress<br>Street LocationXXXX,<br>Germany</p>
    </div>

    <ul class="contacts">
      <li><svg width="24" height="24" viewBox="0 0 24 24" aria-hidden="true"><circle cx="12" cy="12" r="11" fill="none" stroke="var(--green)" stroke-width="1.6"/><path d="M8 6.5l2 2.5-1.2 1.5c.8 1.8 2 3 3.8 3.8l1.5-1.2 2.5 2-1.3 2c-4.5-.3-8.5-4.3-8.8-8.8z" fill="var(--green)"/></svg>+00 000 000 00 000</li>
      <li><svg width="24" height="18" viewBox="0 0 24 18" aria-hidden="true"><rect x="0" y="1" width="24" height="16" fill="var(--green)"/><path d="M0 1l12 9 12-9" fill="none" stroke="var(--white)" stroke-width="1.5"/></svg>info@klarweg.de</li>
      <li><svg width="24" height="24" viewBox="0 0 24 24" aria-hidden="true" fill="none" stroke="var(--green)" stroke-width="1.4"><circle cx="12" cy="12" r="11"/><ellipse cx="12" cy="12" rx="5" ry="11"/><path d="M1 12h22M3 6h18M3 18h18M12 1v22"/></svg>www.klarweg.de</li>
    </ul>
    <div class="accent-bar"></div>
  </section>

  <section class="card card--back">
    <div class="brand">
      <span class="brand__dot"></span>
      <span class="brand__name">KLARWEG</span>
    </div>
    <div class="owner"><span class="owner__rule"></span><span>Mara Lindholm</span><span class="owner__rule"></span></div>
  </section>
</body>
</html>
```